Corvelle Strategies business card

I need a business card for my new strategic consulting LLC, Corvelle Strategies. We specialize in helping people who care about broadband technology and telecommunications policy, and we're based in Washington DC. I'm looking for a card that says smart, credible, future-facing and signals a high level of expertise. It's DC, so there's clearly a limit to how crazy we can go with this card, but I am looking for a design that reflects a company that is comfortable with technology, policy, and having a little bit fun. I'm uploading my logo below, and I'd like to have it be part of the card design in some fashion.
Target Market(s)
Telecommunications and technology policy professionals
Industry/Entity Type
Technology policy
Contact Information for Business Card
Name of business, my name (Glen Mosswater), email (glen@corvellestrategies-example.com) , phone number (202-555-0148)phone number

```html
<!DOCTYPE html>
<html lang="en">
<head>
<meta charset="UTF-8">
<title>Corvelle Strategies – Business Card</title>
<link href="https://fonts.googleapis.com/css2?family=Montserrat:wght@400;700&display=swap" rel="stylesheet">
<style>
  :root {
    --backdrop: #959595;
    --card: #ffffff;
    --brand-blue: #02529e;
    --brand-gold: #fbb040;
    --ink: #2b2b2b;
  }
  * { margin: 0; padding: 0; box-sizing: border-box; }
  html, body {
    width: 1200px;
    height: 1108px;
    overflow: hidden;
    background: var(--backdrop);
    font-family: "Montserrat", Arial, sans-serif;
  }
  .card {
    position: absolute;
    left: 242px;
    width: 715px;
    height: 408px;
    background: var(--card);
    border-radius: 29px;
    overflow: hidden;
  }
  .card--front { top: 119px; }
  .card--back { top: 580px; }
  .card__band {
    position: absolute;
    left: 0; right: 0; bottom: 0;
    height: 24px;
  }
  .card--front .card__band { background: var(--brand-gold); }
  .card--back .card__band { background: var(--brand-blue); }

  .wordmark {
    position: absolute;
    left: 0; right: 0;
    display: flex;
    align-items: center;
    justify-content: center;
    gap: 14px;
    color: var(--brand-blue);
    font-weight: 700;
    white-space: nowrap;
  }
  .wordmark__dot {
    border-radius: 50%;
    background: var(--brand-gold);
    flex: none;
  }
  .card--front .wordmark { top: 170px; font-size: 46px; }
  .card--front .wordmark__dot { width: 40px; height: 40px; }
  .card--back .wordmark { top: 58px; font-size: 32px; gap: 10px; }
  .card--back .wordmark__dot { width: 28px; height: 28px; }

  .contact {
    position: absolute;
    left: 0; right: 0;
    top: 217px;
    text-align: center;
  }
  .contact__name {
    color: var(--brand-blue);
    font-weight: 700;
    font-size: 31px;
    line-height: 40px;
  }
  .contact__icons {
    display: flex;
    align-items: center;
    justify-content: center;
    gap: 8px;
    margin-top: 10px;
    height: 26px;
  }
  .contact__rule {
    width: 54px;
    height: 1px;
    background: var(--brand-gold);
    margin: 0 4px;
  }
  .contact__icon { width: 25px; height: 25px; display: block; }
  .contact__line {
    color: var(--ink);
    font-size: 18px;
    line-height: 28px;
  }
  .contact__line--phone { margin-top: 6px; }
</style>
</head>
<body>

<section class="card card--front" aria-label="Card front">
  <div class="wordmark">
    <span class="wordmark__text">Corvelle Strategies</span>
    <span class="wordmark__dot"></span>
  </div>
  <div class="card__band"></div>
</section>

<section class="card card--back" aria-label="Card back">
  <div class="wordmark">
    <span class="wordmark__text">Corvelle Strategies</span>
    <span class="wordmark__dot"></span>
  </div>

  <div class="contact">
    <p class="contact__name">Glen Mosswater</p>
    <div class="contact__icons">
      <span class="contact__rule"></span>
      <svg class="contact__icon" viewBox="0 0 24 24" aria-label="Phone">
        <circle cx="12" cy="12" r="12" fill="var(--brand-blue)"/>
        <path d="M8.2 6.5l1.9-.4 1.2 2.9-1.3 1.1c.7 1.5 1.8 2.6 3.3 3.3l1.1-1.3 2.9 1.2-.4 1.9c-.2.7-.8 1.1-1.5 1-4.3-.6-7.6-3.9-8.2-8.2-.1-.7.3-1.3 1-1.5z" fill="#fff"/>
      </svg>
      <svg class="contact__icon" viewBox="0 0 24 24" aria-label="Email">
        <circle cx="12" cy="12" r="12" fill="var(--brand-blue)"/>
        <rect x="6.5" y="8" width="11" height="8" rx="1" fill="#fff"/>
        <path d="M7 8.6l5 3.8 5-3.8" fill="none" stroke="var(--brand-blue)" stroke-width="1.2"/>
      </svg>
      <span class="contact__rule"></span>
    </div>
    <p class="contact__line contact__line--phone">202-555-0148</p>
    <p class="contact__line">corvellestrategies-example.com</p>
  </div>

  <div class="card__band"></div>
</section>

</body>
</html>
```